World Class Presentation folder for a National Designer of innovative building products

We are a National Designer, Manufacturer, and distributor of aluminum and stainless Balconies, Railings, Sunshades, and Patio Covers. We sell our products and services to the very best commercial condo and residential builders in the country. This Brochure folder will be the first piece of literature that we give to our customers, and want to WOW them at first glance with a world-class design and look.

We already have a logo and website but would like you to visit https://velmorafabworks.example and view the projects and product information to help inspire you to create an award-winning piece of literature for us.

Besides putting literature in it, the folder must have a place to hold a business card.

Thank you in advance for your great designs, and I look forward to working with you.
Dolan Fratheringe
President | Pacific, WA
418.627.5190 ext 305

```html
<!DOCTYPE html>
<html lang="en">
<head>
<meta charset="utf-8">
<title>Velmora Fabworks Presentation Folder</title>
<link rel="stylesheet" href="https://fonts.googleapis.com/css2?family=Open+Sans:wght@400;600&family=Roboto:wght@400;700&display=swap">
<style>
  :root {
    --crimson: #c41246;
    --crimson-deep: #8e0d33;
    --ink: #141a1e;
    --paper: #ffffff;
    --mist: #d4d4d4;
    --sky: #6f9fd6;
    --cloud: #dfe6ee;
    --foliage: #6d7a4c;
    --street: #4a4a43;
    --text-light: #ffffff;
    --text-dark: #1b1f22;
  }
  html, body { margin: 0; padding: 0; overflow: hidden; background: var(--paper); }
  .canvas { position: relative; width: 1200px; height: 800px; overflow: hidden; background: var(--paper); }
  .dieline { position: absolute; inset: 0; }
  .layer { position: absolute; margin: 0; transform: translateX(-50%); text-align: center; white-space: nowrap; }
  .feature-label { font-family: "Roboto", sans-serif; font-size: 9px; color: var(--text-light); top: 210px; }
  .brand-name { font-family: "Roboto", sans-serif; font-weight: 700; letter-spacing: 1px; line-height: 1.05; }
  .brand-name--inside { top: 313px; left: 434px; font-size: 18px; color: var(--text-light); }
  .brand-name--cover { top: 519px; left: 793px; font-size: 18px; color: var(--crimson); }
  .contact { font-family: "Open Sans", sans-serif; font-size: 6.7px; line-height: 7.8px; color: var(--text-light); }
  .contact--phones { top: 386px; left: 434px; }
  .contact--address { top: 430px; left: 434px; }
  .contact--web { top: 543px; left: 440px; font-size: 7px; }
  .tagline { font-family: "Roboto", sans-serif; font-size: 10.5px; line-height: 14.5px; color: var(--text-light); top: 451px; left: 793px; }
  .cover-phone { font-family: "Roboto", sans-serif; font-weight: 700; font-size: 9px; color: var(--text-dark); top: 111px; left: 930px; }
</style>
</head>
<body>
<main class="canvas">
  <svg class="dieline" width="1200" height="800" viewBox="0 0 1200 800" xmlns="http://www.w3.org/2000/svg">
    <defs>
      <linearGradient id="photoTone" x1="0.15" y1="0" x2="0.35" y2="1">
        <stop offset="0" stop-color="var(--sky)"/>
        <stop offset="0.18" stop-color="var(--cloud)"/>
        <stop offset="0.36" stop-color="#9fb4c4"/>
        <stop offset="0.55" stop-color="var(--foliage)"/>
        <stop offset="0.75" stop-color="var(--street)"/>
        <stop offset="0.9" stop-color="#23292c"/>
        <stop offset="1" stop-color="var(--ink)"/>
      </linearGradient>
      <radialGradient id="emblemTone" cx="0.4" cy="0.35" r="0.75">
        <stop offset="0" stop-color="var(--crimson)"/>
        <stop offset="1" stop-color="var(--crimson-deep)"/>
      </radialGradient>
      <linearGradient id="coverFoot" x1="0" y1="0" x2="1" y2="0">
        <stop offset="0" stop-color="#ffffff"/>
        <stop offset="0.6" stop-color="#ffffff"/>
        <stop offset="1" stop-color="var(--mist)"/>
      </linearGradient>
      <clipPath id="bandClip"><rect x="255" y="489" width="718" height="20"/></clipPath>
    </defs>

    <path class="side-flap" fill="var(--crimson)" d="M255 77 L162 96 Q140 100 140 122 L140 537 Q140 556 162 560 L255 578 Z"/>
    <path class="pocket-flap" fill="var(--crimson)" d="M256 578 L613 578 L573 695 Q566 714 545 714 L367 714 Q360 754 322 754 Q283 754 277 710 Z"/>

    <rect class="back-panel" x="255" y="77" width="359" height="501" fill="var(--ink)"/>

    <rect class="cover-foot" x="614" y="500" width="359" height="78" fill="url(#coverFoot)"/>
    <rect class="cover-photo" x="614" y="77" width="359" height="412" fill="url(#photoTone)" role="img" aria-label="Photograph of a dark aluminum railing on a balcony overlooking city towers and trees"/>
    <rect class="partner-badge" x="901" y="89" width="58" height="18" rx="2" fill="var(--crimson)"/>

    <rect x="255" y="489" width="359" height="19" fill="var(--paper)"/>
    <g clip-path="url(#bandClip)">
      <polygon points="255,501 259,494 357,494 353,501" fill="var(--crimson)"/>
      <polygon points="359,501 363,494 461,494 457,501" fill="var(--ink)"/>
      <polygon points="463,501 467,494 565,494 561,501" fill="var(--crimson)"/>
      <polygon points="567,501 571,494 669,494 665,501" fill="var(--ink)"/>
      <polygon points="671,501 675,494 773,494 769,501" fill="var(--crimson)"/>
      <polygon points="775,501 779,494 877,494 873,501" fill="var(--ink)"/>
      <polygon points="879,501 883,494 981,494 977,501" fill="var(--crimson)"/>
      <polygon points="983,501 987,494 1085,494 1081,501" fill="var(--ink)"/>
    </g>

    <g class="feature-icon">
      <circle cx="326" cy="166" r="29.5" fill="none" stroke="var(--crimson)" stroke-width="3.5"/>
      <circle cx="326" cy="166" r="24" fill="url(#emblemTone)" role="img" aria-label="Stars and stripes emblem"/>
    </g>
    <g class="feature-icon">
      <circle cx="433" cy="166" r="29.5" fill="none" stroke="var(--crimson)" stroke-width="3.5"/>
      <circle cx="433" cy="166" r="24" fill="url(#emblemTone)" role="img" aria-label="Map of the United States"/>
    </g>
    <g class="feature-icon">
      <circle cx="541" cy="166" r="29.5" fill="none" stroke="var(--crimson)" stroke-width="3.5"/>
      <circle cx="541" cy="166" r="24" fill="url(#emblemTone)" role="img" aria-label="Handshake emblem"/>
    </g>

    <circle cx="434" cy="378" r="5" fill="var(--crimson)"/>
    <path d="M432 375.5 q-1 2.5 2.5 5 l1 -1 -1.3 -1.2 -0.8 0.6 q-1.2 -0.9 -1.5 -2.2 l0.7 -0.6 -0.9 -1.4 z" fill="var(--text-light)"/>
    <circle cx="434" cy="424" r="4.5" fill="var(--crimson)"/>
    <path d="M434 421.6 l2.2 2 v2.4 h-4.4 v-2.4 z" fill="var(--text-light)"/>
    <circle cx="382" cy="547" r="4.5" fill="var(--crimson)"/>
    <circle cx="382" cy="547" r="2" fill="none" stroke="var(--text-light)" stroke-width="0.7"/>
  </svg>

  <p class="layer feature-label" style="left:326px">Made In America</p>
  <p class="layer feature-label" style="left:433px">Nationwide Distribution</p>
  <p class="layer feature-label" style="left:541px">Join Us</p>

  <p class="layer brand-name brand-name--inside">VELMORA<br>FABWORKS</p>

  <p class="layer contact contact--phones">418-627-5190<br>866-540-2713</p>
  <p class="layer contact contact--address">Velmora Fabworks - WA<br>742 Corran Ave SE<br>Ashdale, WA 98160</p>
  <p class="layer contact contact--web">www.velmorafabworks.example</p>

  <p class="layer cover-phone">866-540-2713</p>
  <p class="layer tagline">PREMIER MANUFACTURER AND DISTRIBUTER OF<br>ALUMINUM RAILING, BALCONY, AND SUNSHADE SYSTEMS</p>

  <p class="layer brand-name brand-name--cover">VELMORA<br>FABWORKS</p>
</main>
</body>
</html>
```